Design a sleek website for a Global parking app

We need a sleek website for a soon-to-be-launched global parking app called 'Vantly'.

Please see attached specs for the site's three example pages for which we need designs. I have also included:
- Original, high-res versions of the images contained in the Word docs
- Vantly business card
- Vantly logos

Industry/Entity Type

Parking

Coding

Coded - Design and coding required

Number of Pages Required

3 page

Colors
1b1b1b
ffffff

Requirements
Must have
• - Sleek design, which ties in with the brand
• - Complete look and feel for the three key pages spec'd out

```html
<!DOCTYPE html>
<html lang="en">
<head>
<meta charset="utf-8">
<title>Vantly — Your private parking space</title>
<link rel="stylesheet" href="https://fonts.googleapis.com/css2?family=Roboto:wght@400;500;700&display=swap">
<style>
  :root {
    --ink: #1b1b1b;
    --white: #ffffff;
    --accent: #f7c600;
    --accent-soft: #fbe79b;
    --paper: #f0f0f0;
    --muted: #8a8a8a;
    --line: #d8d8d8;
  }
  * { box-sizing: border-box; margin: 0; padding: 0; }
  html, body { width: 851px; height: 1200px; overflow: hidden; }
  body { font-family: "Roboto", Arial, sans-serif; color: var(--ink); background: var(--white); position: relative; }

  .site-header { position: absolute; left: 0; top: 0; width: 851px; height: 87px; background: var(--white); }
  .brand { position: absolute; left: 17px; top: 12px; width: 72px; text-align: center; }
  .brand-mark { display: block; width: 40px; height: 40px; margin: 0 auto; background: var(--ink); }
  .brand-name { display: block; margin-top: 6px; font-size: 11px; letter-spacing: 2px; font-weight: 400; }
  .brand-tagline { display: block; margin-top: 2px; font-size: 5px; white-space: nowrap; }
  .lease-button { position: absolute; left: 426px; top: 17px; width: 199px; height: 29px; border: 2px solid var(--ink); border-radius: 2px; font-size: 11.5px; line-height: 25px; text-align: center; }
  .nav-link { position: absolute; top: 22px; font-size: 11.5px; }
  .nav-help { left: 663px; } .nav-signup { left: 719px; } .nav-login { left: 790px; }

  .hero { position: absolute; left: 0; top: 87px; width: 851px; height: 488px; background: linear-gradient(180deg, #6e625a 0%, #8a8580 35%, #3b3f48 60%, #5c5f63 100%); overflow: hidden; }
  .hero-title { position: absolute; left: 0; top: 113px; width: 851px; text-align: center; font-size: 33px; font-weight: 700; color: var(--white); letter-spacing: 0.5px; }
  .vehicle-types { position: absolute; left: 300px; top: 171px; }
  .vehicle-types svg { display: block; }
  .how-button { position: absolute; left: 366px; top: 247px; width: 120px; height: 39px; background: var(--accent-soft); border: 3px solid var(--white); border-radius: 3px; font-size: 14px; line-height: 33px; text-align: center; }
  .search-band { position: absolute; left: 0; top: 418px; width: 851px; height: 70px; background: rgba(60,60,60,0.55); }
  .search-field { position: absolute; top: 24px; height: 32px; background: var(--white); border-right: 1px solid var(--line); font-size: 14px; color: var(--muted); line-height: 32px; padding-left: 20px; }
  .search-field .caret { display: inline-block; margin-left: 9px; width: 0; height: 0; border-left: 5px solid transparent; border-right: 5px solid transparent; border-top: 6px solid var(--muted); vertical-align: middle; }
  .f-where { left: 33px; width: 251px; } .f-in { left: 284px; width: 133px; padding-left: 28px; } .f-out { left: 417px; width: 134px; } .f-type { left: 551px; width: 149px; padding-left: 16px; }
  .search-button { position: absolute; left: 700px; top: 24px; width: 118px; height: 32px; background: var(--accent); font-size: 14px; line-height: 32px; text-align: center; }

  .lease-section { position: absolute; left: 0; top: 596px; width: 851px; height: 325px; }
  .photo-scooter { position: absolute; left: 0; top: 0; width: 351px; height: 325px; background: linear-gradient(160deg, #c9b89c 0%, #3a8fd0 45%, #1e6fb5 80%, #9a9490 100%); }
  .photo-scooter-caption { position: absolute; left: 54px; top: 234px; width: 260px; font-size: 20px; font-weight: 700; line-height: 25px; color: var(--white); }
  .lease-panel { position: absolute; left: 351px; top: 0; width: 283px; height: 325px; background: var(--accent-soft); }
  .lease-panel p { position: absolute; left: 24px; width: 260px; font-size: 20px; line-height: 25px; }
  .lease-panel .lead { top: 52px; } .lease-panel .body { top: 117px; }
  .learn-button { position: absolute; left: 79px; top: 241px; width: 127px; height: 35px; background: var(--ink); color: var(--white); border-radius: 3px; font-size: 14px; line-height: 35px; text-align: center; }
  .photo-classic-car { position: absolute; left: 634px; top: 0; width: 217px; height: 325px; background: linear-gradient(110deg, #f2f2f2 0%, #c8ccd2 45%, #3d4656 80%, #222630 100%); }

  .explore { position: absolute; left: 0; top: 921px; width: 851px; height: 279px; background: var(--paper); }
  .explore-title { position: absolute; left: 0; top: 20px; width: 960px; text-align: center; font-size: 26px; font-weight: 400; }
  .explore-sub { position: absolute; left: 0; top: 49px; width: 960px; text-align: center; font-size: 20px; }
  .explore-title, .explore-sub { width: 960px; left: -0px; }
  .city-card { position: absolute; top: 92px; height: 167px; }
  .city-card span { position: absolute; left: 0; top: 0; width: 100%; line-height: 167px; text-align: center; font-size: 25px; font-weight: 700; color: var(--white); }
  .city-sydney { left: 34px; width: 250px; background: linear-gradient(180deg, #2a2a2a, #5a5a5a 60%, #1d1d1d); }
  .city-adelaide { left: 301px; width: 250px; background: linear-gradient(180deg, #7fb0e0 0%, #b6d2ea 45%, #6f8a3c 75%, #3f5a22 100%); }
  .city-melbourne { left: 567px; width: 252px; background: linear-gradient(135deg, #c4486a 0%, #5a8fb8 40%, #e0a040 70%, #3d4a5a 100%); }
</style>
</head>
<body>
  <header class="site-header">
    <div class="brand">
      <span class="brand-mark"></span>
      <span class="brand-name">VANTLY</span>
      <span class="brand-tagline">Your private parking space</span>
    </div>
    <div class="lease-button">Lease your parking space for FREE</div>
    <span class="nav-link nav-help">Help</span>
    <span class="nav-link nav-signup">Sign up</span>
    <span class="nav-link nav-login">Login</span>
  </header>

  <section class="hero" role="img" aria-label="Dark sedan parked on a city street beside a brick townhouse and an ornate lamp post">
    <h1 class="hero-title">YOUR PRIVATE PARKING SPACE</h1>
    <div class="vehicle-types">
      <svg width="252" height="56" viewBox="0 0 252 56" fill="none" stroke="#ffffff" stroke-width="1.5">
        <circle cx="25" cy="28" r="24.5"/>
        <circle cx="92" cy="28" r="24.5"/>
        <circle cx="159" cy="28" r="24.5"/>
        <circle cx="225" cy="28" r="24.5"/>
        <g fill="#ffffff" stroke="none">
          <path d="M10 30 L14 22 H34 L39 30 H41 V36 H9 V30 Z"/>
          <circle cx="16" cy="37" r="3"/><circle cx="33" cy="37" r="3"/>
          <path d="M91 14 V35 H78 Z"/><path d="M93 17 V35 H104 Z"/>
          <path d="M76 37 H108 L104 42 H80 Z"/>
          <path d="M147 33 L152 26 H166 L170 33 Z"/><rect x="163" y="20" width="3" height="7"/>
          <circle cx="148" cy="36" r="4"/><circle cx="170" cy="36" r="4"/>
          <ellipse cx="222" cy="30" rx="10" ry="5"/><rect x="206" y="21" width="34" height="2"/>
          <rect x="221" y="22" width="2" height="4"/><path d="M230 29 H244 V31 H230 Z"/>
          <rect x="214" y="37" width="16" height="1.6"/>
        </g>
      </svg>
    </div>
    <div class="how-button">How it works</div>
    <div class="search-band">
      <div class="search-field f-where">Where do you want to park</div>
      <div class="search-field f-in">Check in<span class="caret"></span></div>
      <div class="search-field f-out">Check out<span class="caret"></span></div>
      <div class="search-field f-type">Vehicle type park<span class="caret"></span></div>
      <div class="search-button">Search</div>
    </div>
  </section>

  <section class="lease-section">
    <div class="photo-scooter" role="img" aria-label="Blue scooter parked on a cobbled lane">
      <p class="photo-scooter-caption">Parking your vehicle just got easier</p>
    </div>
    <div class="lease-panel">
      <p class="lead">Leasing your private parking space just made more sense</p>
      <p class="body">Earn money sharing your extra space with people seeking a parking spot like yours.</p>
      <div class="learn-button">Learn more</div>
    </div>
    <div class="photo-classic-car" role="img" aria-label="Close-up of a classic car's chrome headlight"></div>
  </section>

  <section class="explore">
    <h2 class="explore-title" style="width:851px">Explore the world of VANTLY</h2>
    <p class="explore-sub" style="width:851px">See where other people are parking.</p>
    <div class="city-card city-sydney" role="img" aria-label="Rows of parked bicycles in Sydney"><span>Sydney</span></div>
    <div class="city-card city-adelaide" role="img" aria-label="Vineyard and timber post under blue sky near Adelaide"><span>Adelaide</span></div>
    <div class="city-card city-melbourne" role="img" aria-label="Scooter parked in front of a graffiti laneway in Melbourne"><span>Melbourne</span></div>
  </section>
</body>
</html>
```